Stationery and Business Card Design

We need stationary design for our new company pelvanta. Pelvanta is a company that provides city apartment rentals for tourists in Athens We need business cards, letterheads for A4 and A5 and envelopes for A4 A5. The design needs to be modern, friendly and corporate.

Target Market(s)

City Tourists

Industry/Entity Type

Tourism

```html
<!DOCTYPE html>
<html lang="en">
<head>
<meta charset="utf-8">
<title>Pelvanta Stationery</title>
<link rel="stylesheet" href="https://fonts.googleapis.com/css2?family=Raleway:wght@400;600&family=Roboto:wght@400;500&display=swap">
<style>
  :root {
    --brand: #92004f;
    --brand-soft: #a8336f;
    --ink: #1f1f1f;
    --band-dark: #3d3d3f;
    --backdrop: #e3e3e5;
    --paper: #ffffff;
  }
  * { margin: 0; padding: 0; box-sizing: border-box; }
  html, body { width: 1189px; height: 1200px; overflow: hidden; background: var(--backdrop); }
  body { position: relative; font-family: "Roboto", Arial, sans-serif; color: var(--ink); }

  .sheet { position: absolute; background: var(--paper); overflow: hidden; }
  .bands { position: absolute; left: 0; bottom: 0; width: 100%; }

  .brand { position: absolute; display: flex; flex-direction: column; align-items: center; }
  .brand-square { background: var(--brand); }
  .brand-name { font-family: "Raleway", Arial, sans-serif; font-weight: 400; color: var(--brand); line-height: 1; }

  /* Letterhead */
  .letterhead { left: 50px; top: 110px; width: 507px; height: 657px; }
  .letterhead .brand { left: 55px; top: 37px; width: 170px; }
  .letterhead .brand-square { width: 50px; height: 50px; }
  .letterhead .brand-name { font-size: 30px; margin-top: 10px; }
  .contact { position: absolute; right: 61px; top: 58px; text-align: right; font-family: "Raleway", Arial, sans-serif; font-size: 8.5px; line-height: 10.5px; color: #333; }
  .contact .gap { height: 6px; }
  .contact .row { display: flex; justify-content: flex-end; align-items: center; gap: 3px; }
  .icon { display: inline-block; width: 7px; height: 7px; background: var(--brand); }
  .recipient { position: absolute; left: 55px; top: 187px; font-size: 8.5px; line-height: 10.5px; }
  .recipient strong { display: block; font-weight: 500; font-size: 10px; margin-bottom: 4px; }
  .body-text { position: absolute; left: 55px; top: 256px; width: 391px; font-size: 8.6px; line-height: 15px; letter-spacing: -0.15px; }
  .body-text p + p { margin-top: 15px; }
  .closing { position: absolute; left: 55px; top: 513px; font-size: 8.6px; }
  .signature { position: absolute; left: 55px; top: 533px; width: 120px; height: 40px; background: linear-gradient(90deg, #e9e9ea, #f4f4f5); }
  .signer { position: absolute; left: 55px; top: 576px; font-size: 8.6px; line-height: 12px; }
  .signer strong { font-weight: 500; font-size: 10px; }

  /* Folder */
  .folder { left: 629px; top: 111px; width: 506px; height: 654px; background: var(--brand); }
  .folder .brand { left: 153px; top: 279px; width: 200px; }
  .folder .brand-square { width: 50px; height: 50px; background: var(--paper); }
  .folder .brand-name { color: var(--paper); font-size: 31px; margin-top: 10px; }

  /* A5 letterhead */
  .a5 { left: 51px; top: 833px; width: 331px; height: 234px; }
  .a5 .brand { left: 18px; top: 23px; width: 96px; }
  .a5 .brand-square { width: 28px; height: 28px; }
  .a5 .brand-name { font-size: 17px; margin-top: 6px; }
  .a5-address { position: absolute; left: 18px; top: 200px; font-size: 3.6px; line-height: 4.4px; color: #555; }

  /* Envelope */
  .envelope { left: 472px; top: 832px; width: 332px; height: 235px; background: transparent; overflow: visible; }
  .envelope-body { position: absolute; inset: 0; background: var(--paper); }
  .envelope .flap { position: absolute; left: 0; top: 0; width: 332px; height: 55px; }
  .envelope .brand { left: 116px; top: 12px; width: 100px; }
  .envelope .brand-name { color: var(--paper); font-size: 20px; margin-top: 6px; }

  /* Business cards */
  .card-back { left: 921px; top: 805px; width: 215px; height: 122px; }
  .card-pattern { position: absolute; inset: 0; background: linear-gradient(135deg, #8b0a4d, #9a1a5c); }
  .card-back .brand { left: 60px; top: 44px; width: 95px; }
  .card-back .brand-name { color: var(--paper); font-size: 20px; font-weight: 400; }
  .card-front { left: 921px; top: 953px; width: 215px; height: 122px; }
  .card-front .brand { left: 9px; top: 13px; width: 88px; }
  .card-front .brand-square { width: 25px; height: 25px; }
  .card-front .brand-name { font-size: 16px; margin-top: 5px; }
  .employee { position: absolute; right: 10px; top: 72px; text-align: right; }
  .employee strong { display: block; font-family: "Raleway", Arial, sans-serif; font-weight: 600; font-size: 8px; color: var(--brand); }
  .employee span { display: block; font-size: 5.5px; color: #555; margin-top: -1px; }
  .employee-rule { position: absolute; left: 9px; right: 66px; top: 79px; height: 0; border-top: 0.6px solid #999; }
  .card-contact { position: absolute; left: 10px; top: 92px; font-size: 5.4px; line-height: 7.2px; color: #444; }
  .card-contact .row { display: flex; align-items: center; gap: 2px; }
  .card-contact .icon { width: 5px; height: 5px; }
  .card-address { position: absolute; right: 10px; top: 99px; text-align: right; font-size: 5.4px; line-height: 7.2px; color: #444; }
</style>
</head>
<body>

<section class="sheet letterhead" aria-label="A4 letterhead">
  <div class="brand">
    <div class="brand-square"></div>
    <div class="brand-name">Pelvanta</div>
  </div>
  <address class="contact">
    <div>0000 Your Address, 2nd Ste.</div>
    <div>Ardley, Vestria 1234</div>
    <div class="gap"></div>
    <div class="row">210 555 0147 <span class="icon"></span></div>
    <div class="row">hello@pelvanta-stays.com <span class="icon"></span></div>
    <div class="row">www.pelvanta-stays.com <span class="icon"></span></div>
  </address>
  <div class="recipient">
    <strong>MARA VELIS</strong>
    Street Name, City Name.<br>Zip Code 0000
  </div>
  <div class="body-text">
    <p>Lorem Ipsum is simply dummy text of the printing and typesetting industry. Lorem Ipsum has the been the industry's standard dummy text ever since the 1500s, when an unknown printer took a galley of type and scrambled it to make a type specimen book. It has survived not only five centuries, but also the leap into electronic typesetting, remaining essentially unchanged. It was popularised in the 1960s with the release of Letraset sheets containing Lorem Ipsum passages, and more recently with desktop publishing software like Aldus PageMaker including versions of Lorem Ipsum.</p>
    <p>It is a long established fact that a reader will be distracted by the readable content of a page when looking at its layout. The point of using Lorem Ipsum is that it has a more-or-less normal distribution of letters, as opposed to using 'Content here, content here', making it look like readable English. Many desktop publishing packages and web page editors now use Lorem Ipsum as their default model text, and a search for 'lorem ipsum' will uncover many web sites still in their infancy. Various versions have evolved over the years, sometimes by accident, sometimes on purpose (injected humour and the like).</p>
  </div>
  <div class="closing">Regards,</div>
  <div class="signature" role="img" aria-label="Handwritten signature"></div>
  <div class="signer"><strong>Teo Andras</strong><br>General Manager</div>
  <svg class="bands" width="507" height="22" viewBox="0 0 507 22">
    <polygon points="0,7 314,7 308,21 0,21" fill="var(--band-dark)"/>
    <polygon points="322,0 507,0 507,21 314,21" fill="var(--brand)"/>
  </svg>
</section>

<section class="sheet folder" aria-label="Presentation folder">
  <div class="brand">
    <div class="brand-square"></div>
    <div class="brand-name">Pelvanta</div>
  </div>
</section>

<section class="sheet a5" aria-label="A5 letterhead">
  <div class="brand">
    <div class="brand-square"></div>
    <div class="brand-name">Pelvanta</div>
  </div>
  <address class="a5-address">0000 Your Address, 2nd Ste.<br>Ardley, Vestria 1234</address>
  <svg class="bands" width="331" height="13" viewBox="0 0 331 13">
    <polygon points="0,4 203,4 199,13 0,13" fill="var(--band-dark)"/>
    <polygon points="209,0 331,0 331,13 201,13" fill="var(--brand)"/>
  </svg>
</section>

<section class="sheet envelope" aria-label="Envelope">
  <div class="envelope-body"></div>
  <svg class="flap" width="332" height="55" viewBox="0 0 332 55">
    <path d="M0,0 H332 L326,46 Q325,52 318,52 H14 Q7,52 6,46 Z" fill="var(--brand)"/>
  </svg>
  <div class="brand"><div class="brand-name">Pelvanta</div></div>
</section>

<section class="sheet card-back" aria-label="Business card back">
  <div class="card-pattern" role="img" aria-label="Repeating brand pattern in deep magenta"></div>
  <div class="brand"><div class="brand-name">Pelvanta</div></div>
</section>

<section class="sheet card-front" aria-label="Business card front">
  <div class="brand">
    <div class="brand-square"></div>
    <div class="brand-name">Pelvanta</div>
  </div>
  <div class="employee-rule"></div>
  <div class="employee"><strong>Employee Name</strong><span>Principal Consultant</span></div>
  <address class="card-contact">
    <div class="row"><span class="icon"></span> 000 000 0000</div>
    <div class="row"><span class="icon"></span> team@pelvanta-stays.com</div>
    <div class="row"><span class="icon"></span> www.pelvanta-stays.com</div>
  </address>
  <address class="card-address">0000 Your Address, 2nd Ste.<br>Ardley, Vestria 1234</address>
  <svg class="bands" width="215" height="7" viewBox="0 0 215 7">
    <polygon points="0,2 133,2 131,7 0,7" fill="var(--band-dark)"/>
    <polygon points="138,0 215,0 215,7 134,7" fill="var(--brand)"/>
  </svg>
</section>

</body>
</html>
```